5 year service award card*

I'm attaching a celebration type card in which I need a new card similar made but with VRK logo's on it instead.

Colors

Designer to choose colors to be used in the design.

```html
<!DOCTYPE html>
<html lang="en">
<head>
<meta charset="utf-8">
<title>VRK – 5 Year Service Award</title>
<link rel="stylesheet" href="https://fonts.googleapis.com/css2?family=Cabin+Condensed:wght@600&family=Questrial&display=swap">
<style>
  :root {
    --paper: #ffffff;
    --panel-blue: #729fd0;
    --band-blue: #3f7bbd;
    --brand-blue: #377cc0;
    --band-grey: #dcdde0;
    --slate: #566d7c;
    --message: #ede2e8;
    --shadow: rgba(40, 40, 40, 0.75);
  }
  * { margin: 0; padding: 0; box-sizing: border-box; }
  html, body {
    width: 1200px; height: 849px; overflow: hidden;
    background: var(--paper);
  }
  .card {
    position: relative; width: 1200px; height: 849px; overflow: hidden;
    background: var(--paper);
  }
  .photo-panel {
    position: absolute; left: 35px; top: 37px; width: 497px; height: 779px;
    border: 1px solid #3a3a3a;
    background:
      radial-gradient(ellipse 60% 22% at 30% 14%, rgba(246, 214, 140, 0.75), transparent 70%),
      radial-gradient(ellipse 70% 30% at 50% 88%, rgba(246, 226, 170, 0.8), transparent 70%),
      linear-gradient(180deg, #dfe3e2 0%, #ece0c8 22%, #e4dbe4 45%, #d9cdd6 62%, #d9cfbf 80%, #e8dcc0 100%);
    box-shadow: 8px 7px 7px var(--shadow);
  }
  .message-panel {
    position: absolute; left: 529px; top: 37px; width: 641px; height: 779px;
    background: var(--panel-blue);
    box-shadow: 9px 7px 7px var(--shadow);
  }
  .bands { position: absolute; inset: 0; width: 1200px; height: 849px; }
  .wordmark {
    position: absolute; left: 10px; top: 205px;
    font-family: "Questrial", sans-serif;
    font-size: 250px; line-height: 1; letter-spacing: -8px;
    color: var(--brand-blue);
  }
  .values {
    position: absolute; left: 88px; top: 514px;
    list-style: none;
    font-family: "Questrial", sans-serif;
    font-size: 48px; line-height: 57px;
    color: var(--slate);
    font-weight: 700;
    letter-spacing: 0.5px;
  }
  .values .initial { color: var(--brand-blue); }
  .message {
    position: absolute; left: 569px; top: 88px; width: 600px;
    text-align: center;
    font-family: "Cabin Condensed", sans-serif;
    font-weight: 600; font-size: 43.5px; line-height: 95.5px;
    color: var(--message);
    letter-spacing: -0.5px;
  }
</style>
</head>
<body>
<main class="card">
  <div class="photo-panel" role="img" aria-label="Industrial refinery lit up at dusk under a soft golden and lavender sky"></div>
  <div class="message-panel"></div>

  <svg class="bands" viewBox="0 0 2292 1624" preserveAspectRatio="none" aria-hidden="true">
    <polygon class="band-diagonal" points="975,0 1270,0 1030,272" fill="var(--band-blue)"/>
    <rect class="band-vertical" x="944" y="450" width="61" height="1174" fill="var(--band-blue)"/>
    <polygon class="band-grey" points="690,0 925,0 1100,455 1100,1592 1035,1592 1035,650 680,75" fill="var(--band-grey)"/>
  </svg>

  <div class="wordmark">VRK</div>

  <ul class="values">
    <li><span class="initial">V</span>alues.</li>
    <li><span class="initial">R</span>eliability.</li>
    <li><span class="initial">K</span>nowledge.</li>
    <li><span class="initial">S</span>afety</li>
  </ul>

  <p class="message">
    Thank you for being part<br>
    of our Company’s success<br>
    over these 5 years.<br>
    We greatly appreciate and value<br>
    your hard work and<br>
    commitment to making it work right<br>
    the first time.
  </p>
</main>
</body>
</html>
```